A5 Magazine Cover Design

I need a front cover designing for a new community magazine called QUELBY. QUELBY will be listing local buisnesses and local interest articles for the residents in my area. I need the look to be clean but inviting.

I will consider any colour combination as long as its not too bright.

```html
<!DOCTYPE html>
<html lang="en">
<head>
<meta charset="utf-8">
<title>QUELBY — Community Magazine Cover</title>
<link rel="stylesheet" href="https://fonts.googleapis.com/css2?family=Open+Sans:wght@400;800&display=swap">
<style>
  :root {
    --hill-light: #aa9f91;
    --hill-dark: #655b53;
    --masthead-yellow: #f6b81b;
    --tagline-white: #ffffff;
  }
  html, body {
    margin: 0;
    padding: 0;
    width: 900px;
    height: 1200px;
    overflow: hidden;
  }
  .cover {
    position: relative;
    width: 900px;
    height: 1200px;
    overflow: hidden;
    font-family: "Open Sans", sans-serif;
  }
  .hillside-scene {
    position: absolute;
    inset: 0;
    background: repeating-linear-gradient(
      170deg,
      var(--hill-light) 0px,
      var(--hill-light) 110px,
      var(--hill-dark) 150px,
      var(--hill-dark) 260px,
      var(--hill-light) 300px
    );
  }
  .spine {
    position: absolute;
    left: 0;
    top: 1200px;
    width: 1200px;
    height: 900px;
    transform-origin: 0 0;
    transform: rotate(-90deg);
  }
  .masthead {
    position: absolute;
    left: 4px;
    top: -58px;
    margin: 0;
    font-size: 336px;
    line-height: 1;
    font-weight: 800;
    color: var(--masthead-yellow);
    white-space: nowrap;
    letter-spacing: 0.01em;
  }
  .tagline {
    position: absolute;
    left: 10px;
    top: 250px;
    margin: 0;
    font-size: 44px;
    line-height: 1;
    font-weight: 400;
    color: var(--tagline-white);
    white-space: nowrap;
  }
</style>
</head>
<body>
  <main class="cover">
    <div class="hillside-scene" role="img" aria-label="Repeating illustration of rolling grey hills topped with small white, orange and magenta houses, with white and teal clouds"></div>
    <div class="spine">
      <h1 class="masthead">QUELBY</h1>
      <p class="tagline">QUELBY Searches, Reviews and Recommends Locally.</p>
    </div>
  </main>
</body>
</html>
```